Brookmere Osteopathy flyer

I want a clean clear DL flyer (but also want an A4 poster) promoting a new Osteopathic business in a semi rural area in Tasmania (Australia).
It can have pictures like the examples attached to show people what Osteopathy is (its like Chiropractic and physiotherapy).
I am the sole practioner and am male, so any pictures would be best to be a white male if possible.
I've attached some wording, you can use all, or none of it
I don't have a phone number for the business yet
info@brookmereosteopathy.example
www.brookmereosteopathy.example
Target Market(s)
Australians, from tradies, professionals, babies to retired people
Industry/Entity Type
Health
Look and feel

```html
<!DOCTYPE html>
<html lang="en">
<head>
<meta charset="utf-8">
<title>Brookmere Osteopathy Flyer</title>
<link rel="stylesheet" href="https://fonts.googleapis.com/css2?family=Poppins:wght@400;500;600;700;800&display=swap">
<style>
  :root {
    --navy: #0b2470;
    --blue: #1592d1;
    --orange: #f7913a;
    --ink: #111318;
    --muted: #2b2d33;
    --line: #c9ccd3;
    --paper: #ffffff;
    --photo-light: #dfe3e6;
    --photo-mid: #b9c7cc;
  }
  * { box-sizing: border-box; margin: 0; padding: 0; }
  html, body { width: 682px; height: 1200px; overflow: hidden; }
  body {
    font-family: "Poppins", sans-serif;
    background: var(--paper);
    color: var(--ink);
  }
  .flyer {
    position: relative;
    width: 682px;
    height: 1200px;
    background: radial-gradient(ellipse at 50% 30%, #ffffff 40%, #f1f2f4 100%);
    overflow: hidden;
  }
  .brand {
    position: absolute; top: 70px; left: 0; width: 100%;
    display: flex; justify-content: center; align-items: center; gap: 10px;
  }
  .brand-dot { width: 16px; height: 16px; border-radius: 50%; background: var(--blue); }
  .brand-name { font-size: 24px; font-weight: 600; color: var(--blue); letter-spacing: 0.02em; }
  .headline { position: absolute; top: 140px; left: 0; width: 100%; text-align: center; }
  .headline span { display: block; }
  .headline-top { font-size: 58px; font-weight: 500; color: var(--navy); line-height: 62px; }
  .headline-main { font-size: 92px; font-weight: 800; color: var(--navy); line-height: 84px; letter-spacing: -0.01em; }
  .headline-accent {
    font-size: 48px; font-weight: 600; color: var(--orange); line-height: 60px;
    letter-spacing: 0.6em; padding-left: 0.6em;
  }
  .tagline {
    position: absolute; top: 352px; left: 0; width: 100%; text-align: center;
    font-size: 23px; font-weight: 500; line-height: 29px; color: var(--ink);
  }
  .hero { position: absolute; top: 422px; left: 186px; width: 310px; height: 310px; }
  .hero-ring { position: absolute; inset: 0; border-radius: 50%; border: 8px solid var(--orange); }
  .hero-photo {
    position: absolute; inset: 12px; border-radius: 50%;
    background: linear-gradient(160deg, var(--photo-mid) 0%, var(--photo-light) 55%, #f4f5f6 100%);
  }
  .hero-spine {
    position: absolute; top: 680px; left: 160px; width: 362px; height: 40px;
    border-radius: 20px;
    background: linear-gradient(90deg, #5bb6e3, var(--blue), #5bb6e3);
  }
  .reasons {
    position: absolute; top: 752px; left: 44px; width: 594px; height: 256px;
    border: 1.5px solid var(--line); border-radius: 12px;
  }
  .reasons-title {
    position: absolute; top: -15px; left: 50%; transform: translateX(-50%);
    background: #fff; padding: 0 12px; text-align: center; white-space: nowrap;
    font-weight: 700; font-size: 24px; line-height: 26px;
  }
  .reasons-title span { display: block; }
  .reasons-title .line-1 { color: var(--navy); }
  .reasons-title .line-2 { color: var(--blue); }
  .reasons-list {
    position: absolute; top: 52px; left: 18px; right: 10px;
    display: grid; grid-template-columns: 296px 1fr; row-gap: 10px; list-style: none;
  }
  .reason {
    display: flex; align-items: center; gap: 10px; height: 28px;
    font-size: 16.5px; line-height: 18px; color: var(--ink);
  }
  .reason.two-line { height: 38px; }
  .reason-icon {
    flex: none; width: 26px; height: 26px; border-radius: 50%;
    background: var(--navy); box-shadow: -3px 0 0 var(--orange);
  }
  .reason-icon.warm { background: var(--orange); box-shadow: 3px 0 0 var(--navy); }
  .method {
    position: absolute; top: 1024px; left: 50%; transform: translateX(-50%);
    background: var(--navy); color: #fff; border-radius: 16px;
    font-size: 14px; font-weight: 700; line-height: 18px; padding: 5px 24px; white-space: nowrap;
  }
  .method-text {
    position: absolute; top: 1058px; left: 0; width: 100%; text-align: center;
    font-size: 13.5px; line-height: 17px; color: var(--muted);
  }
  .contact {
    position: absolute; top: 1108px; left: 40px; right: 20px;
    display: grid; grid-template-columns: 272px 1fr; row-gap: 8px;
    font-size: 15px; line-height: 20px; color: var(--ink);
  }
  .contact-item { display: flex; align-items: center; gap: 6px; white-space: nowrap; }
  .contact-item svg { flex: none; }
  .contact-item strong { font-weight: 700; }
  .base-band { position: absolute; bottom: 0; left: 0; width: 100%; height: 14px; background: var(--navy); }
</style>
</head>
<body>
<main class="flyer">
  <header class="brand">
    <span class="brand-dot"></span>
    <span class="brand-name">Brookmere Osteopathy</span>
  </header>

  <h1 class="headline">
    <span class="headline-top">YOUR BODY</span>
    <span class="headline-main">DESERVES</span>
    <span class="headline-accent">RELIEF</span>
  </h1>

  <p class="tagline">Professional osteopathic care for pain,<br>tension, and everyday discomfort.</p>

  <div class="hero">
    <div class="hero-ring"></div>
    <div class="hero-photo" role="img" aria-label="Photo of an osteopath treating a patient lying on her side on a treatment table"></div>
  </div>
  <div class="hero-spine" role="img" aria-label="Blue spine illustration curving beneath the photo"></div>

  <section class="reasons">
    <h2 class="reasons-title">
      <span class="line-1">COMMON REASONS PEOPLE</span>
      <span class="line-2">VISIT AN OSTEOPATH</span>
    </h2>
    <ul class="reasons-list">
      <li class="reason"><span class="reason-icon"></span>Back / neck pain</li>
      <li class="reason"><span class="reason-icon"></span>Sciatica</li>
      <li class="reason"><span class="reason-icon warm"></span>Headaches / migraines</li>
      <li class="reason"><span class="reason-icon warm"></span>Plantar fasciitis</li>
      <li class="reason"><span class="reason-icon"></span>Joint and muscle pain</li>
      <li class="reason"><span class="reason-icon"></span>Tendonitis / Bursitis</li>
      <li class="reason two-line"><span class="reason-icon warm"></span>Pregnancy-related<br>discomfort</li>
      <li class="reason two-line"><span class="reason-icon warm"></span>Adhesive capsulitis<br>(frozen shoulder)</li>
      <li class="reason"><span class="reason-icon"></span>Disc related issues</li>
      <li class="reason"><span class="reason-icon"></span>Tennis / Golfers elbow</li>
    </ul>
  </section>

  <div class="method">OSTEOPATHS USE A COMBINATION OF JOINT MANIPULATION</div>
  <p class="method-text">Targeted deep tissue massage and stretching to improve function,<br>relieve pain and support the body’s ability to heal itself.</p>

  <footer class="contact">
    <div class="contact-item">
      <svg width="12" height="12" viewBox="0 0 24 24"><path fill="#1592d1" d="M6.6 10.8a15.1 15.1 0 0 0 6.6 6.6l2.2-2.2c.3-.3.7-.4 1-.2 1.1.4 2.3.6 3.6.6.6 0 1 .4 1 1V20c0 .6-.4 1-1 1A17 17 0 0 1 3 4c0-.6.4-1 1-1h3.5c.6 0 1 .4 1 1 0 1.3.2 2.5.6 3.6.1.3 0 .7-.2 1z"/></svg>
      <span><strong>CALL US NOW:</strong> 000.555.0142</span>
    </div>
    <div class="contact-item">
      <svg width="12" height="10" viewBox="0 0 24 18"><rect x="1" y="1" width="22" height="16" rx="2" fill="#1592d1"/><path d="M2 2l10 8 10-8" stroke="#fff" stroke-width="2" fill="none"/></svg>
      <span>info@brookmereosteopathy.example</span>
    </div>
    <div class="contact-item">
      <svg width="12" height="15" viewBox="0 0 24 30"><path fill="#1592d1" d="M12 0a10 10 0 0 0-10 10c0 7.5 10 20 10 20s10-12.5 10-20A10 10 0 0 0 12 0zm0 14a4 4 0 1 1 0-8 4 4 0 0 1 0 8z"/></svg>
      <span>24 Ridgeway Lane, Brookmere</span>
    </div>
    <div class="contact-item">
      <svg width="12" height="12" viewBox="0 0 24 24" fill="none" stroke="#1592d1" stroke-width="2"><circle cx="12" cy="12" r="10"/><path d="M2 12h20M12 2c3 3 3 17 0 20M12 2c-3 3-3 17 0 20"/></svg>
      <span>www.brookmereosteopathy.example</span>
    </div>
  </footer>

  <div class="base-band"></div>
</main>
</body>
</html>
```